Corwin Ashgrove

I am a songwriter and would like to include a bio, pictures, discography, CD covers and access to some of my music

Target Market(s)

Music Lovers, songwriters publishers

Coding

Coded - Design and coding required

Number of Pages Required

5+ page

Requirements
Must have
• Pictures of my CD covers, pictures of me and either my Music or links to my music
Nice to have
Should not have
• cartoons

```html
<!DOCTYPE html>
<html lang="en">
<head>
<meta charset="utf-8">
<title>Corwin Ashgrove — Songwriter</title>
<link rel="stylesheet" href="https://fonts.googleapis.com/css2?family=Abril+Fatface&family=Lato:ital,wght@0,400;0,700;1,400&display=swap">
<style>
:root{
  --orange:#f7860e;
  --dark:#121212;
  --ink:#222;
  --navy:#1a3a8a;
  --grey-bg:#f1f1f1;
  --white:#fff;
  --frame:#1c2fa0;
}
*{box-sizing:border-box;margin:0;padding:0}
html,body{width:1200px;height:3077px;overflow:hidden;background:#fff}
body{font-family:"Lato",sans-serif;color:var(--ink);position:relative}
.display{font-family:"Abril Fatface",serif;letter-spacing:1px;text-transform:uppercase}
.btn{position:absolute;display:flex;align-items:center;justify-content:center;font-weight:700;font-size:14px;color:#fff;background:var(--orange);width:154px;height:44px;text-transform:uppercase}

/* hero */
.hero{position:absolute;left:0;top:0;width:1200px;height:680px;background:linear-gradient(90deg,#3a1303 0%,#b4440b 25%,#e26a12 45%,#5a2110 65%,#2a160e 100%)}
.hero-photo{position:absolute;left:640px;top:100px;width:460px;height:580px;background:radial-gradient(ellipse at 45% 35%,#c99a80 0%,#6a4a3c 35%,#2b1e1a 70%,transparent 72%)}
.logo{position:absolute;left:75px;top:36px;color:#fff;font-size:27px;line-height:32px}
.nav{position:absolute;top:60px;left:317px;display:flex;gap:42px;font-size:13px;color:#fff}
.nav .active{color:var(--orange)}
.hi{position:absolute;left:75px;top:222px;color:#fff;font-style:italic;font-size:34px}
.hero h1{position:absolute;left:75px;top:258px;color:#fff;font-size:64px;font-weight:700}
.hero p{position:absolute;left:75px;top:334px;color:#fff;font-size:19px;line-height:26px}
.hero .btn{left:75px;top:405px;background:var(--dark)}
.player{position:absolute;left:310px;top:611px;width:580px;height:48px;border:5px solid #555;background:#2a2a2a;border-radius:4px}

/* about */
.about-photo{position:absolute;left:75px;top:733px;width:234px;height:283px;background:linear-gradient(160deg,#a07a4a,#6b4c2c 50%,#c9b49a)}
.about h2{position:absolute;left:343px;top:728px;font-size:29px;color:var(--ink)}
.about .body{position:absolute;left:343px;top:776px;width:780px;font-size:13.5px;line-height:22.5px}
.about .body p+p{margin-top:13px}
.about .btn{left:343px;top:972px}

/* what i do */
.what{position:absolute;left:0;top:1087px;width:1200px;height:366px;background:linear-gradient(120deg,#2a2826,#4a4540 50%,#1e1c1a)}
.what h2{position:absolute;top:88px;width:100%;text-align:center;color:#fff;font-size:29px}
.what p{position:absolute;left:75px;top:136px;width:1050px;text-align:center;color:#fff;font-size:13.5px;line-height:22.5px}
.what .btn{left:523px;top:228px}

/* discography */
.disco h2{position:absolute;top:1493px;width:100%;text-align:center;font-size:29px}
.card{position:absolute;width:241px}
.cover{width:241px;height:177px;border:3px solid var(--frame)}
.card h3{margin-top:17px;text-align:center;font-size:15px}
.card span{display:block;text-align:center;font-size:12px;font-weight:700;margin-top:4px}

/* events */
.events{position:absolute;left:0;top:2104px;width:1200px;height:396px;background:var(--grey-bg)}
.events h2{position:absolute;top:52px;width:100%;text-align:center;font-size:29px}
.event{position:absolute;top:130px;width:330px}
.event .date{font-family:"Abril Fatface",serif;color:var(--navy);font-size:15px}
.event h3{font-weight:400;font-size:20px;margin-top:4px}
.event p{font-size:13.5px;line-height:22.5px;margin-top:6px}
.divider{position:absolute;top:132px;width:1px;height:114px;background:#bbb}
.events .btn{left:523px;top:292px}

/* reviews */
.reviews{position:absolute;left:0;top:2500px;width:1200px;height:405px;background:linear-gradient(140deg,#1a1a1a,#3a3a3a 50%,#141414)}
.reviews h2{position:absolute;top:64px;width:100%;text-align:center;color:#fff;font-size:29px}
.reviews blockquote{position:absolute;left:100px;top:130px;width:1000px;text-align:center;color:#fff;font-size:18.5px;line-height:34.5px}
.reviews cite{position:absolute;top:248px;width:100%;text-align:center;color:var(--orange);font-style:normal;font-size:15px}
.arrows{position:absolute;left:557px;top:316px}

/* footer */
.foot-nav{position:absolute;top:2948px;width:100%;display:flex;justify-content:center;gap:47px;font-size:15px}
.copy{position:absolute;top:2981px;width:100%;text-align:center;font-size:15px}
.social{position:absolute;top:3013px;width:100%;display:flex;justify-content:center;gap:18px}
.social i{width:22px;height:22px;border-radius:50%;background:var(--orange);display:block}
</style>
</head>
<body>

<header class="hero">
  <div class="hero-photo" role="img" aria-label="Photo of the songwriter standing at night before a glowing fire pit"></div>
  <div class="logo display">Corwin<br>Ashgrove</div>
  <nav class="nav display">
    <span class="active">Home</span><span>About Corwin Ashgrove</span><span>Discography</span><span>Upcoming Events</span><span>Reviews</span><span>Contact Us</span>
  </nav>
  <div class="hi">Hi I Am,</div>
  <h1>Corwin Ashgrove</h1>
  <p>Maecenas urna elit, tincidunt in dapibus nec,<br>vehicula eu dui uis lacinia.</p>
  <a class="btn">Read More</a>
  <div class="player">
    <svg width="570" height="38" viewBox="0 0 570 38">
      <polygon points="28,13 28,25 37,19" fill="#fff"/>
      <rect x="48" y="13" width="3" height="12" fill="#fff"/><rect x="54" y="13" width="3" height="12" fill="#fff"/>
      <rect x="67" y="13" width="12" height="12" fill="#fff"/>
      <rect x="105" y="17" width="367" height="4" fill="#ccc"/>
      <rect x="105" y="17" width="158" height="4" fill="#ff1f4e"/>
      <polygon points="496,16 500,16 505,12 505,26 500,22 496,22" fill="#fff"/>
      <circle cx="523" cy="19" r="5" fill="none" stroke="#fff" stroke-width="2.5"/>
      <path d="M542 25 L552 15 M548 14 L553 14 L553 19 M541 20 L541 25 L546 25" stroke="#fff" stroke-width="2" fill="none"/>
    </svg>
  </div>
</header>

<section class="about">
  <div class="about-photo" role="img" aria-label="Portrait of the songwriter in a white shirt holding a hat"></div>
  <h2 class="display">About Corwin Ashgrove</h2>
  <div class="body">
    <p>Corwin Ashgrove was born and raised in Houston, Texas. He began playing music at the age of eight when his sister returned home from summer camp and asked her parents to buy her a baritone ukulele. She taught her younger brother some chords on the ukulele and he was hooked. The following spring, they went to one of the border towns in Mexico and bought a Mexican guitar for $12. They restrung it with nylon strings and Ashgrove began to learn how to play the guitar.</p>
    <p>He took guitar lessons at a local music store and learned how to play the hits of the day by groups like the Larkspur Five, the Tin Lanterns, and the Quarry Boys. He got his first electric guitar when he was about 10 years old. He began jamming with other musicians when he was 13 or 14. They were much more experienced than he and introduced him to the blues.</p>
  </div>
  <a class="btn">Read More</a>
</section>

<section class="what" role="img" aria-label="Background photo of a hand writing song notes beside a guitar">
  <h2 class="display">What I Do</h2>
  <p>Maecenas tempus eros ut diam ullamcorper id dictum libero tempor. Donec quis augue quis magna condimentum lobortis. Quisque imperdiet ipsum vel magna viverra rutrum. Cras viverra molestie urna, vitae vestibulum turpis varius id.Vestibulum mollis, arcu iaculis bibendum varius, velit sapien blandit metus, ac posuere lorem nulla ac dolor. Maecenas urna elit, tincidunt in dapibus nec, vehicula eu dui. Duis lacinia fringilla massa.</p>
  <a class="btn">Read More</a>
</section>

<section class="disco">
  <h2 class="display">Corwin Ashgrove Discography</h2>
  <div class="card" style="left:75px;top:1551px"><div class="cover" role="img" aria-label="Album cover: silhouette under lightning over burning ruins" style="background:linear-gradient(160deg,#5a5a70,#2a1a18 50%,#a03a10)"></div><h3 class="display">Maecenas</h3><span>Oct 30,2020</span></div>
  <div class="card" style="left:344px;top:1551px"><div class="cover" role="img" aria-label="Album cover: pastel collage with a child photo" style="background:linear-gradient(135deg,#e8e6f4,#f4e0d8 50%,#d8d2e8)"></div><h3 class="display">Maecenas</h3><span>Oct 30,2020</span></div>
  <div class="card" style="left:616px;top:1551px"><div class="cover" role="img" aria-label="Album cover: ship on a stormy sea" style="background:linear-gradient(180deg,#7a8088,#3a4450 55%,#1e2a34)"></div><h3 class="display">Maecenas</h3><span>Oct 30,2020</span></div>
  <div class="card" style="left:885px;top:1551px"><div class="cover" role="img" aria-label="Album cover: flames over a diner table with coffee cup" style="background:linear-gradient(135deg,#d03a10,#f09030 45%,#c8b090)"></div><h3 class="display">Maecenas</h3><span>Oct 30,2020</span></div>
  <div class="card" style="left:75px;top:1819px"><div class="cover" role="img" aria-label="Album cover: guitarist in vivid psychedelic colours" style="background:linear-gradient(135deg,#20c0a0,#80d040 50%,#e04020)"></div><h3 class="display">Maecenas</h3><span>Oct 30,2020</span></div>
  <div class="card" style="left:344px;top:1819px"><div class="cover" role="img" aria-label="Album cover: black and white band photo with track list" style="background:linear-gradient(135deg,#1a1a1a,#555 60%,#111)"></div><h3 class="display">Maecenas</h3><span>Oct 30,2020</span></div>
  <div class="card" style="left:616px;top:1819px"><div class="cover" role="img" aria-label="Album cover: silhouette under lightning over burning ruins" style="background:linear-gradient(160deg,#5a5a70,#2a1a18 50%,#a03a10)"></div><h3 class="display">Maecenas</h3><span>Oct 30,2020</span></div>
  <div class="card" style="left:885px;top:1819px"><div class="cover" role="img" aria-label="Album cover: pastel collage with a child photo" style="background:linear-gradient(135deg,#e8e6f4,#f4e0d8 50%,#d8d2e8)"></div><h3 class="display">Maecenas</h3><span>Oct 30,2020</span></div>
</section>

<section class="events">
  <h2 class="display">Upcoming Events</h2>
  <div class="event" style="left:75px"><div class="date">DEC 01, 2020</div><h3>Cras viverra molestie</h3><p>Lorem ipsum dolor sit amet, consectetur adipiscing elit. Nulla est purus, ultrices in porttitor in, accumsan non quam.</p></div>
  <div class="divider" style="left:405px"></div>
  <div class="event" style="left:435px"><div class="date">DEC 01, 2020</div><h3>Cras viverra molestie</h3><p>Lorem ipsum dolor sit amet, consectetur adipiscing elit. Nulla est purus, ultrices in porttitor in, accumsan non quam.</p></div>
  <div class="divider" style="left:766px"></div>
  <div class="event" style="left:794px"><div class="date">DEC 01, 2020</div><h3>Cras viverra molestie</h3><p>Lorem ipsum dolor sit amet, consectetur adipiscing elit. Nulla est purus, ultrices in porttitor in, accumsan non quam.</p></div>
  <a class="btn">View All Events</a>
</section>

<section class="reviews" role="img" aria-label="Dark background photo of a desk with laptop and coffee">
  <h2 class="display">Reviews</h2>
  <blockquote>“ At this point I have developed a continuous creative relationship with Corwin and have recorded on approximately 30 songs of his. He writes well-structured songs that allow me to flex my creative muscles. Corwin knows how to make his original ideas blossom into fully constructed arrangements that sound great..”</blockquote>
  <cite class="display">Tomas Reyvald, Lowline Studios</cite>
  <svg class="arrows" width="86" height="20" viewBox="0 0 86 20">
    <path d="M24 10 H3 M10 3 L3 10 L10 17" stroke="#fff" stroke-width="3" fill="none"/>
    <path d="M60 10 H83 M76 3 L83 10 L76 17" stroke="#fff" stroke-width="3" fill="none"/>
  </svg>
</section>

<footer>
  <nav class="foot-nav display"><span>Home</span><span>About Corwin Ashgrove</span><span>Discography</span><span>Upcoming Events</span><span>Reviews</span><span>Contact Us</span></nav>
  <div class="copy">Copyright © 2020 CompanyName&nbsp; All rights reserved.</div>
  <div class="social"><i></i><i></i><i></i><i></i><i></i></div>
</footer>

</body>
</html>
```